Intuitive, look stunning website design for the street-level digital media platform that connects audiences with dynamic media on taxis and rideshare vehicles on BACK AND SIDE WINDOWS OF THE VEHICLE. SO FOOT TRAFFIC AND ALL OTHER TRAFFIC CAN SEE DISPLAY ON MOVING VEHICLE (in the future high glass building glass concept)
There should be 7 tabs VORTELANE as home button, advertisers, partners, drivers, about us, news and contact.

Target Market(s)

The company works with taxi companies and rideshare drivers to install its proprietary advertising displays in their vehicles. These proprietary screens deliver dynamic content based on location-based, WiFi-enabled triggers.

Vortelane provides an additional revenue stream to maximize drive time and empowers brands to efficiently engage consumers across our nation's busiest cities, including San Francisco, Los Angeles, New York City, Dallas, Austin, Chicago and Miami.

Industry/Entity Type

Digital Marketing

Coding

Coded - Design and coding required

Number of Pages Required

5+ page

Font styles to use
Sans Serif

Requirements
Must have
• Use beautiful graphics and easy to read fonts.
Make sure graphics are compressed and optimized for fast loading.
Design should be consistent on brand throughout the website design.
Design an intuitive navigation system which allows users to get to the pages they need quickly.
Create pages that are standard for all business from small to big such; home, about us, product/services , sitemap ( seo purposes) contact us etc..
icons links for snapchat, instagram, client login, facbook
Nice to have
• Out of box concept
Should not have
• ITS NOT AN LCD BOX PLACED OVER THE CAR

```html
<!DOCTYPE html>
<html lang="en">
<head>
<meta charset="utf-8">
<title>Vortelane — Street-Level Digital Media</title>
<link href="https://fonts.googleapis.com/css2?family=Montserrat:wght@800;900&family=Roboto:wght@400;500;700&display=swap" rel="stylesheet">
<style>
:root{
  --navy:#0a3f8c;
  --blue:#1f7fc4;
  --ink:#1d1d1d;
  --text:#333;
  --soft:#f4f1f1;
  --footer:#262626;
  --white:#fff;
}
*{box-sizing:border-box;margin:0;padding:0}
html,body{width:1200px;height:3002px;overflow:hidden}
body{position:relative;font-family:'Roboto',sans-serif;color:var(--text);background:var(--white)}
.abs{position:absolute}
a{color:inherit;text-decoration:none}

/* header */
.site-header{position:absolute;left:0;top:0;width:1200px;height:128px;background:var(--white)}
.brand{position:absolute;left:130px;top:40px;display:flex;align-items:center;gap:10px}
.brand-dot{width:30px;height:30px;border-radius:50%;background:var(--navy)}
.brand-name{font-family:'Roboto',sans-serif;font-weight:500;font-size:22px;letter-spacing:3px;color:var(--ink)}
.client-login{position:absolute;left:629px;top:38px;width:117px;height:30px;background:var(--blue);color:#fff;border-radius:4px;font-size:12px;font-weight:700;display:flex;align-items:center;justify-content:center}
.top-label{position:absolute;top:23px;font-size:12px;font-weight:700;color:var(--navy)}
.social-top{position:absolute;left:775px;top:38px;display:flex;gap:3px}
.social-top span{width:32px;height:32px;background:var(--navy);border-radius:5px;display:flex;align-items:center;justify-content:center}
.social-top span i{width:10px;height:10px;border-radius:50%;background:#fff;display:block}
.phone-box{position:absolute;left:907px;top:38px;width:162px;height:32px;background:var(--blue);border-radius:5px;color:#fff;display:flex;align-items:center;gap:8px;padding-left:10px;font-size:19px;font-weight:500}
.main-nav{position:absolute;right:127px;top:93px;display:flex;gap:34px;font-size:14px;font-weight:500;color:var(--ink)}
.main-nav .active{color:var(--navy);text-decoration:underline;text-underline-offset:3px;font-weight:700}

/* hero */
.hero{position:absolute;left:0;top:128px;width:1200px;height:538px;background:linear-gradient(180deg,#8e8f8c 0%,#b9b6ad 40%,#e0a11f 45%,#e8a828 70%,#6b6a66 85%,#4a4a48 100%)}
.hero-panel{position:absolute;left:0;top:68px;width:370px;height:98px;background:rgba(10,63,140,.88);clip-path:polygon(0 0,360px 0,370px 100%,0 100%)}
.hero-title{position:absolute;left:52px;top:82px;font-family:'Montserrat',sans-serif;font-weight:900;font-size:25px;color:#fff}
.hero-sub{position:absolute;left:80px;top:114px;font-size:14px;color:#fff}
.hero-btn{position:absolute;left:245px;top:142px;width:95px;height:27px;background:var(--blue);color:#fff;font-size:12px;font-weight:700;display:flex;align-items:center;justify-content:center}
.dots{position:absolute;left:0;width:1200px;top:496px;display:flex;justify-content:center;gap:10px;align-items:center}
.dots i{width:8px;height:8px;border-radius:50%;background:#fff;display:block}
.dots i.on{width:12px;height:12px;border:2px solid #fff;background:var(--blue)}

/* section titles */
.section-title{position:absolute;left:0;width:1200px;text-align:center;font-size:24px;font-weight:700;color:var(--ink)}
.title-rule{position:absolute;left:576px;width:48px;height:2px;background:var(--navy)}

/* services */
.service-card{position:absolute;top:836px;width:299px;height:259px;background:#fff;box-shadow:0 1px 5px rgba(0,0,0,.18);text-align:center}
.service-icon{position:absolute;left:107px;top:-35px;width:86px;height:86px;border-radius:50%;background:var(--blue);display:flex;align-items:center;justify-content:center}
.service-card h3{position:absolute;top:76px;width:100%;font-size:16px;font-weight:700;color:var(--blue)}
.service-card p{position:absolute;top:112px;left:40px;width:225px;font-size:13px;line-height:17.6px;color:var(--text)}

/* welcome */
.welcome-photo{position:absolute;left:0;top:1150px;width:604px;height:412px;background:linear-gradient(135deg,#5c6068 0%,#8c8a86 35%,#eaa326 55%,#d38d17 70%,#4f5258 100%)}
.welcome-body{position:absolute;left:604px;top:1150px;width:596px;height:412px;background:var(--soft)}
.welcome-kicker{position:absolute;left:41px;top:46px;font-size:18px;font-weight:500;color:var(--ink)}
.welcome-title{position:absolute;left:41px;top:72px;font-size:30px;font-weight:700;color:var(--ink);letter-spacing:.5px}
.welcome-rule{position:absolute;left:41px;top:126px;width:38px;height:2px;background:var(--ink)}
.welcome-text{position:absolute;left:41px;top:162px;width:420px;font-size:14.5px;line-height:19.2px;color:var(--text)}
.btn-navy{position:absolute;background:var(--navy);color:#fff;font-size:14px;font-weight:500;display:flex;align-items:center;justify-content:center}

/* news */
.news{position:absolute;left:0;top:1562px;width:1200px;height:477px;background:var(--navy)}
.news .section-title{color:#fff;top:45px}
.news .title-rule{background:var(--blue);top:84px}
.news-card{position:absolute;top:133px;width:294px;height:233px;background:#fff;border-top:6px solid var(--blue);padding:34px 37px}
.news-date{font-size:12.5px;font-weight:700;color:var(--ink)}
.news-text{margin-top:18px;font-size:15.5px;line-height:20px;color:var(--text)}
.news-btn{margin-top:16px;display:inline-block;border:2px solid var(--navy);color:var(--navy);font-size:12px;font-weight:700;padding:5px 12px}
.news-arrows{position:absolute;left:0;width:1200px;top:404px;display:flex;justify-content:center;align-items:center;gap:14px;color:#fff}
.news-arrows i{width:1px;height:18px;background:#fff;display:block}

/* split promo */
.promo{position:absolute;top:2039px;height:332px;text-align:center;color:#fff}
.promo h2{position:absolute;left:0;width:100%;top:108px;font-family:'Montserrat',sans-serif;font-weight:800;font-size:30px}
.promo p{position:absolute;left:0;width:100%;top:144px;font-size:15px}
.promo .promo-btn{position:absolute;top:181px;width:110px;height:35px;background:var(--blue);color:#fff;font-size:13.5px;font-weight:500;display:flex;align-items:center;justify-content:center}
.promo-advertisers{left:0;width:598px;background:linear-gradient(160deg,#3e3f42 0%,#6b6a66 40%,#b98a2a 65%,#4a4a48 100%)}
.promo-drivers{left:598px;width:602px;background:linear-gradient(200deg,#4a3c28 0%,#8a6f2a 40%,#c79a25 60%,#3d3a36 100%)}

/* partners */
.partner-row{position:absolute;left:130px;top:2525px;width:940px;height:60px;display:flex;justify-content:space-between;align-items:center}
.partner{font-size:22px;font-weight:700;color:#111;width:150px;text-align:center}
.partner-arrow{position:absolute;top:2540px}

/* footer */
.site-footer{position:absolute;left:0;top:2654px;width:1200px;height:348px;background:var(--footer);color:#e6e6e6}
.footer-brand{position:absolute;left:186px;top:108px;display:flex;align-items:center;gap:10px}
.footer-brand .brand-dot{background:#fff}
.footer-brand .brand-name{color:#fff}
.footer-col{position:absolute;top:48px}
.footer-col h4{font-size:13px;font-weight:700;color:#fff;letter-spacing:.3px}
.footer-menu{list-style:none;margin-top:20px;font-size:12px;line-height:19.8px}
.footer-item{display:flex;align-items:flex-start;gap:10px;font-size:12px;line-height:15.5px}
.footer-icon{width:24px;height:24px;border-radius:50%;background:#fff;display:flex;align-items:center;justify-content:center;flex:none;margin-top:3px}
.footer-rule{position:absolute;left:130px;top:262px;width:939px;height:1px;background:#3a3a3a}
.copyright{position:absolute;left:0;width:1200px;top:305px;text-align:center;font-size:11px;color:#ddd}
</style>
</head>
<body>

<header class="site-header">
  <a class="brand" href="#"><span class="brand-dot"></span><span class="brand-name">VORTELANE</span></a>
  <a class="client-login" href="#">CLIENT LOGIN</a>
  <span class="top-label" style="left:775px">FOLLOW US</span>
  <div class="social-top" aria-label="Social links">
    <span><i></i></span><span><i></i></span><span><i></i></span>
  </div>
  <span class="top-label" style="left:907px">CALL US</span>
  <div class="phone-box">
    <svg width="16" height="16" viewBox="0 0 24 24"><path fill="#fff" d="M6.6 10.8a15 15 0 0 0 6.6 6.6l2.2-2.2c.3-.3.7-.4 1-.2 1.1.4 2.3.6 3.6.6.6 0 1 .4 1 1V20c0 .6-.4 1-1 1C10.6 21 3 13.4 3 4c0-.6.4-1 1-1h3.5c.6 0 1 .4 1 1 0 1.3.2 2.5.6 3.6.1.3 0 .7-.2 1z"/></svg>
    555.010.2040
  </div>
  <nav class="main-nav">
    <a class="active" href="#">HOME</a><a href="#">ADVERTISERS</a><a href="#">PARTNERS</a><a href="#">DRIVERS</a><a href="#">ABOUT US</a><a href="#">NEWS</a><a href="#">CONTACT</a>
  </nav>
</header>

<section class="hero" role="img" aria-label="Yellow taxi parked on a city street with a rooftop digital advertising display">
  <div class="hero-panel"></div>
  <h1 class="hero-title">ADVERTISING DISPLAYS</h1>
  <p class="hero-sub">LOREM IPSUM IS SIMPLY DUMMY TEXT</p>
  <a class="hero-btn" href="#">READ MORE</a>
  <div class="dots"><i></i><i></i><i class="on"></i><i></i><i></i></div>
</section>

<h2 class="section-title" style="top:713px">OUR SERVICES</h2>
<div class="title-rule" style="top:753px"></div>

<article class="service-card" style="left:130px">
  <div class="service-icon">
    <svg width="40" height="44" viewBox="0 0 40 44"><rect x="6" y="2" width="28" height="36" rx="2" fill="none" stroke="#fff" stroke-width="3"/><path d="M12 11h16M12 17h16M12 23h16M12 29h10" stroke="#fff" stroke-width="2.5"/><circle cx="28" cy="36" r="5" fill="#fff"/></svg>
  </div>
  <h3>LOREM IPSUM</h3>
  <p>Lorem Ipsum is simply dummy text of the printing and typesetting ind ustry 'lorem ipsum' will uncover many web sites still in their generators on the Internet tend to repeat pred efined chunks</p>
</article>
<article class="service-card" style="left:451px">
  <div class="service-icon">
    <svg width="50" height="34" viewBox="0 0 50 34"><rect x="1" y="6" width="8" height="20" fill="#fff"/><rect x="41" y="6" width="8" height="20" fill="#fff"/><path d="M10 10l10-4 6 4 6-4 8 4v12l-12 8-18-8z" fill="none" stroke="#fff" stroke-width="3" stroke-linejoin="round"/></svg>
  </div>
  <h3>LOREM IPSUM</h3>
  <p>Lorem Ipsum is simply dummy text of the printing and typesetting ind ustry 'lorem ipsum' will uncover many web sites still in their generators on the Internet tend to repeat pred efined chunks</p>
</article>
<article class="service-card" style="left:771px">
  <div class="service-icon">
    <svg width="44" height="44" viewBox="0 0 44 44"><rect x="3" y="3" width="17" height="17" fill="#fff"/><rect x="23" y="3" width="17" height="17" fill="none" stroke="#fff" stroke-width="3"/><rect x="3" y="23" width="17" height="17" fill="none" stroke="#fff" stroke-width="3"/><rect x="23" y="23" width="17" height="17" fill="#fff"/></svg>
  </div>
  <h3>LOREM IPSUM</h3>
  <p>Lorem Ipsum is simply dummy text of the printing and typesetting ind ustry 'lorem ipsum' will uncover many web sites still in their generators on the Internet tend to repeat pred efined chunks</p>
</article>

<div class="welcome-photo" role="img" aria-label="Yellow taxi driving fast through a busy city crosswalk"></div>
<section class="welcome-body">
  <p class="welcome-kicker">WELCOME TO</p>
  <h2 class="welcome-title">VORTELANE</h2>
  <div class="welcome-rule"></div>
  <p class="welcome-text">Lorem ipsum dolor sit amet, consectetur adipiscing elit, sed do eiusmod tempor incididunt ut labore et dolore magna aliqua. Ut enim ad minim veniam, quis nostrud exercitation ullamco laboris nisi ut aliquip ex ea commodo consequat. Duis aute irure dolor in reprehenderit in voluptate velit esse cillum dolore eu fugiat nulla pariatur. Excepteur sint occaecat cupidatat non proident, sunt in culpa qui officia deserunt mollit anim id est laborum.</p>
  <a class="btn-navy" href="#" style="left:44px;top:331px;width:111px;height:35px">READ MORE</a>
</section>

<section class="news">
  <h2 class="section-title">LATEST NEWS</h2>
  <div class="title-rule"></div>
  <article class="news-card" style="left:130px">
    <p class="news-date">AUG 24, 2020</p>
    <p class="news-text">Sed ut perspiciatis unde omnis iste natus error sit voluptatem accusantium doloremque laud antium, totam rem.</p>
    <a class="news-btn" href="#">READ MORE</a>
  </article>
  <article class="news-card" style="left:453px">
    <p class="news-date">AUG 24, 2020</p>
    <p class="news-text">Sed ut perspiciatis unde omnis iste natus error sit voluptatem accusantium doloremque laud antium, totam rem.</p>
    <a class="news-btn" href="#">READ MORE</a>
  </article>
  <article class="news-card" style="left:776px">
    <p class="news-date">AUG 24, 2020</p>
    <p class="news-text">Sed ut perspiciatis unde omnis iste natus error sit voluptatem accusantium doloremque laud antium, totam rem.</p>
    <a class="news-btn" href="#">READ MORE</a>
  </article>
  <div class="news-arrows">
    <svg width="18" height="10" viewBox="0 0 18 10"><path d="M17 5H2M6 1L2 5l4 4" fill="none" stroke="#fff" stroke-width="1.6"/></svg>
    <i></i>
    <svg width="18" height="10" viewBox="0 0 18 10"><path d="M1 5h15M12 1l4 4-4 4" fill="none" stroke="#fff" stroke-width="1.6"/></svg>
  </div>
</section>

<section class="promo promo-advertisers" role="img" aria-label="Yellow taxi with a rooftop sign in city traffic">
  <h2>ADVERTISERS</h2>
  <p>Lorem Ipsum is simply dummy text of the</p>
  <a class="promo-btn" href="#" style="left:248px">READ MORE</a>
</section>
<section class="promo promo-drivers" role="img" aria-label="Smiling taxi driver seated behind the wheel of a yellow cab">
  <h2>DRIVERS</h2>
  <p>Lorem Ipsum is simply dummy text of the</p>
  <a class="promo-btn" href="#" style="left:246px">READ MORE</a>
</section>

<h2 class="section-title" style="top:2427px">OUR PARTNERS</h2>
<div class="title-rule" style="top:2467px"></div>
<svg class="partner-arrow" style="left:68px" width="14" height="28" viewBox="0 0 14 28"><path d="M12 2L2 14l10 12" fill="none" stroke="#aaa" stroke-width="2"/></svg>
<div class="partner-row">
  <span class="partner">Halden</span>
  <span class="partner">Stridewell</span>
  <span class="partner">Paperline</span>
  <span class="partner">Genova</span>
  <span class="partner">Coinly</span>
</div>
<svg class="partner-arrow" style="left:1118px" width="14" height="28" viewBox="0 0 14 28"><path d="M2 2l10 12L2 26" fill="none" stroke="#aaa" stroke-width="2"/></svg>

<footer class="site-footer">
  <div class="footer-brand"><span class="brand-dot"></span><span class="brand-name">VORTELANE</span></div>

  <div class="footer-col" style="left:451px">
    <h4>MENU</h4>
    <ul class="footer-menu">
      <li>HOME</li><li>ADVERTISERS</li><li>PARTNERS</li><li>DRIVERS</li><li>ABOUT US</li><li>NEWS</li><li>CONTACT</li>
    </ul>
  </div>

  <div class="footer-col" style="left:666px">
    <h4>CONTACT US</h4>
    <div class="footer-item" style="margin-top:20px">
      <span class="footer-icon"><svg width="10" height="13" viewBox="0 0 10 13"><path d="M5 0a5 5 0 0 0-5 5c0 3.7 5 8 5 8s5-4.3 5-8a5 5 0 0 0-5-5zm0 7a2 2 0 1 1 0-4 2 2 0 0 1 0 4z" fill="#262626"/></svg></span>
      <span>P.O. BOX 40417<br>HARBOR STATION<br>MERIDALE, CA 90210-0417</span>
    </div>
    <div class="footer-item" style="margin-top:11px">
      <span class="footer-icon"><svg width="12" height="12" viewBox="0 0 24 24"><path fill="#262626" d="M6.6 10.8a15 15 0 0 0 6.6 6.6l2.2-2.2c.3-.3.7-.4 1-.2 1.1.4 2.3.6 3.6.6.6 0 1 .4 1 1V20c0 .6-.4 1-1 1C10.6 21 3 13.4 3 4c0-.6.4-1 1-1h3.5c.6 0 1 .4 1 1 0 1.3.2 2.5.6 3.6.1.3 0 .7-.2 1z"/></svg></span>
      <span>Call Us<br>555.010.2040</span>
    </div>
    <div class="footer-item" style="margin-top:19px">
      <span class="footer-icon"><svg width="12" height="9" viewBox="0 0 12 9"><rect width="12" height="9" rx="1" fill="#262626"/><path d="M0.5 0.8L6 5l5.5-4.2" fill="none" stroke="#fff" stroke-width="1"/></svg></span>
      <span>E mail us<br>info@vortelane.com</span>
    </div>
  </div>

  <div class="footer-col" style="left:961px">
    <h4>FOLLOW US</h4>
    <div class="footer-item" style="margin-top:20px"><span class="footer-icon"></span><span>Like us on<br>FRIENDWALL</span></div>
    <div class="footer-item" style="margin-top:19px"><span class="footer-icon"></span><span>Follow us on<br>CHIRPLINE</span></div>
    <div class="footer-item" style="margin-top:19px"><span class="footer-icon"></span><span>Follow us on<br>WORKFOLD</span></div>
  </div>

  <div class="footer-rule"></div>
  <p class="copyright">Copyright © 2020 All Rights Reserved</p>
</footer>

</body>
</html>
```